Design a New Business Card for Our Company

We are looking for fresh, unique, and a modern business card that reflects our roots as digital marketing agency focused on SEM.

Industry/Entity Type

Marketing

Contact Information for Business Card

looking for very unique out of the box designs. clean and modern that compliments our logo

Requirements
Must have
• colors should match our logo
• Front should have name, address, email, and phone/fax of the person, phone/fax are the same number
• back should have our url

```html
<!DOCTYPE html>
<html lang="en">
<head>
<meta charset="utf-8">
<title>Brightway Media – Business Card</title>
<link rel="stylesheet" href="https://fonts.googleapis.com/css2?family=Open+Sans:wght@400;600;700&display=swap">
<style>
  :root {
    --page-bg: #ecebe8;
    --card-white: #ffffff;
    --card-grey: #b4b3b3;
    --pattern-grey: #a9a8a8;
    --brand-blue: #4d8ad0;
    --brand-grey: #a3a3a3;
    --ink: #2f2f2f;
    --shadow: rgba(0, 0, 0, 0.18);
  }
  * { box-sizing: border-box; margin: 0; padding: 0; }
  html, body {
    width: 1200px;
    height: 900px;
    overflow: hidden;
    background: var(--page-bg);
    font-family: "Open Sans", Arial, sans-serif;
  }
  .canvas {
    position: relative;
    width: 1200px;
    height: 900px;
  }
  .card {
    position: absolute;
    top: 295px;
    width: 540px;
    height: 310px;
    border-radius: 3px;
    box-shadow: 0 8px 24px var(--shadow);
    overflow: hidden;
  }

  /* Back of card */
  .card-back {
    left: 40px;
    background: var(--card-grey);
    color: #fff;
  }
  .card-back .pattern-area {
    position: absolute;
    inset: 0;
    background: linear-gradient(160deg, var(--card-grey), var(--pattern-grey));
  }
  .card-back .brand {
    position: absolute;
    left: 0;
    right: 0;
    top: 108px;
    text-align: center;
    font-size: 46px;
    font-weight: 700;
    letter-spacing: -1px;
    line-height: 1;
  }
  .card-back .url {
    position: absolute;
    left: 0;
    right: 0;
    top: 196px;
    text-align: center;
    font-size: 15px;
    font-weight: 700;
  }

  /* Front of card */
  .card-front {
    left: 620px;
    background: var(--card-white);
    color: var(--ink);
  }
  .contact {
    position: absolute;
    left: 292px;
    right: 20px;
    top: 34px;
    font-size: 12.5px;
    line-height: 1.3;
    white-space: nowrap;
  }
  .contact .name {
    color: var(--brand-blue);
    font-size: 17px;
    font-weight: 700;
  }
  .contact .role { margin-bottom: 26px; padding-left: 6px; }
  .contact .address { margin-bottom: 20px; padding-left: 24px; }
  .contact .lines { list-style: none; padding-left: 36px; }
  .contact .lines li {
    display: flex;
    align-items: center;
    gap: 6px;
    margin-bottom: 3px;
  }
  .contact .lines svg { width: 11px; height: 11px; flex: none; }
  .brand-mark {
    position: absolute;
    left: 40px;
    bottom: 44px;
    display: flex;
    align-items: center;
    gap: 12px;
  }
  .brand-mark .dot {
    width: 34px;
    height: 34px;
    border-radius: 50%;
    background: var(--brand-blue);
  }
  .brand-mark .brand {
    color: var(--brand-grey);
    font-size: 36px;
    font-weight: 700;
    letter-spacing: -1px;
    line-height: 1;
  }
</style>
</head>
<body>
<main class="canvas">

  <section class="card card-back" aria-label="Card back">
    <div class="pattern-area" role="img" aria-label="Soft scattered circle pattern in grey tones"></div>
    <p class="brand">Brightway Media</p>
    <p class="url">www.brightwaymedia.com</p>
  </section>

  <section class="card card-front" aria-label="Card front">
    <div class="contact">
      <p class="name">Daniel Brooks</p>
      <p class="role">Managing Director</p>
      <p class="address">48 Harbour Lane, Suite 210<br>Eastport, 20415</p>
      <ul class="lines">
        <li>
          <svg viewBox="0 0 12 12" aria-hidden="true"><path fill="#4d8ad0" d="M2.4 1l2 2.3-1 1.3c.7 1.5 1.7 2.5 3.1 3.2l1.3-1 2.2 2-1.1 1.9C4.6 10.5 1.3 7.3.7 2.1z"/></svg>
          (044)-555-0142
        </li>
        <li>
          <svg viewBox="0 0 12 12" aria-hidden="true"><rect x="3" y="1" width="6" height="3.5" fill="#4d8ad0"/><rect x="1" y="5" width="10" height="6" rx="1" fill="#4d8ad0"/><rect x="3.5" y="7" width="5" height="2" fill="#fff"/></svg>
          555-010-4477
        </li>
        <li>
          <svg viewBox="0 0 12 12" aria-hidden="true"><rect x="0.5" y="2.5" width="11" height="7.5" fill="#4d8ad0"/><path d="M1 3l5 3.6L11 3" fill="none" stroke="#fff" stroke-width="1"/></svg>
          hello@brightwaymedia.com
        </li>
      </ul>
    </div>
    <div class="brand-mark">
      <span class="dot"></span>
      <span class="brand">Brightway Media</span>
    </div>
  </section>

</main>
</body>
</html>
```